Copper Ridge Business Cards For New Startup

I am looking for you to design some business cards for a new startup https://copperridgehub.example. I have supplied logo, brand guidelines and our signatures as a guide.

We need this to reflect the brand guidelines and the website for brand consistency,

What is Copper Ridge?

Mallorca's Business Growth Community
Join your new business community full of passionate entrepreneurs who
love to solve problems and help each other grow together!

Any questions you can ask.

Target Market(s)

Business to Business

Contact Information for Business Card

These are attached (signatures) to the job

Font styles to use
Other font styles liked:
• Open Sans

Requirements
Must have
• Match design guidelines
Nice to have
• Photos of our faces so people remember us

```html
<!DOCTYPE html>
<html lang="en">
<head>
<meta charset="utf-8">
<title>Copper Ridge Business Cards</title>
<link href="https://fonts.googleapis.com/css2?family=Open+Sans:wght@400;600;700&display=swap" rel="stylesheet">
<style>
  :root {
    --olive: #5f6300;
    --olive-text: #5b5a05;
    --ink: #3b3b3b;
    --paper: #ffffff;
    --backdrop: #3a3c3f;
    --rule: #9a9a9a;
  }
  * { box-sizing: border-box; margin: 0; padding: 0; }
  html, body {
    width: 1200px; height: 1000px; overflow: hidden;
    background: var(--backdrop);
    font-family: "Open Sans", Arial, sans-serif;
  }
  .card {
    position: absolute;
    width: 700px; height: 400px;
    background: var(--paper);
    overflow: hidden;
  }
  .card--back { left: 300px; top: 60px; }
  .card--front { left: 200px; top: 540px; }

  /* brand mark stand-in */
  .brand-seal {
    position: absolute;
    width: 176px; height: 176px;
    border-radius: 50%;
    background: var(--paper);
    border: 6px solid var(--olive);
    display: flex; align-items: center; justify-content: center;
    text-align: center;
    color: var(--olive);
    font-weight: 700;
    font-size: 22px;
    line-height: 1.15;
  }
  .card--back .brand-seal { left: 262px; top: 70px; }
  .card--front .brand-seal { left: 300px; top: 62px; }

  /* back */
  .back-stripe {
    position: absolute; left: 0; right: 0; bottom: 44px;
    height: 36px;
    background: var(--olive);
    display: flex; align-items: center;
    padding-left: 250px;
  }
  .back-url {
    color: var(--paper);
    font-size: 18px;
    letter-spacing: 4px;
  }

  /* front */
  .front-band {
    position: absolute; left: 0; top: 0; right: 0;
    height: 150px;
    background: var(--olive);
  }
  .identity {
    position: absolute; right: 395px; top: 255px;
    text-align: right;
    color: var(--olive-text);
  }
  .identity__name {
    font-size: 28px; font-weight: 700; letter-spacing: 0.5px;
    line-height: 1.1;
  }
  .identity__role, .identity__company {
    font-size: 19px; line-height: 1.3;
  }
  .divider {
    position: absolute; left: 330px; top: 262px;
    width: 2px; height: 104px;
    background: var(--rule);
  }
  .contact {
    position: absolute; left: 355px; top: 256px;
    font-size: 18px; line-height: 1.3;
    color: var(--ink);
    list-style: none;
  }
  .contact__label { color: var(--olive-text); font-weight: 700; margin-right: 6px; }
  .social {
    position: absolute; left: 355px; top: 342px;
    display: flex; gap: 9px;
    list-style: none;
  }
  .social__item {
    width: 34px; height: 34px;
    border-radius: 4px;
    background: var(--olive);
  }
</style>
</head>
<body>
  <section class="card card--back" aria-label="Business card back">
    <div class="brand-seal">Copper<br>Ridge</div>
    <div class="back-stripe"><span class="back-url">copperridgehub.example</span></div>
  </section>

  <section class="card card--front" aria-label="Business card front">
    <div class="front-band"></div>
    <div class="brand-seal">Copper<br>Ridge</div>

    <div class="identity">
      <p class="identity__name">DANIEL MARSH</p>
      <p class="identity__role">Founder &amp; Growth Hacker</p>
      <p class="identity__company">Copper Ridge</p>
    </div>

    <div class="divider"></div>

    <ul class="contact">
      <li><span class="contact__label">M:</span>+34 611 482 307</li>
      <li><span class="contact__label">E:</span>dm@copperridgehub.example</li>
      <li><span class="contact__label">W:</span>copperridgehub.example</li>
    </ul>

    <ul class="social" aria-label="Social profiles">
      <li class="social__item"></li>
      <li class="social__item"></li>
      <li class="social__item"></li>
      <li class="social__item"></li>
      <li class="social__item"></li>
    </ul>
  </section>
</body>
</html>
```